Business Card Design for a technology company

Our current business card is outdated and stale.

We need a new look and one soon.

We're a telematics (GPS tracking) company based in Australia. Our audiences are transport and logistics company.

Target Market(s)

1. Transport and Logistics Companies
2. Food and Beverage Manufacturers
3. Concrete Businesses

Industry/Entity Type

Logistics

Contact Information for Business Card

Halvor Pinet

Font styles to use
Sans Serif

Colors
3276b5
0255a3
85acd3
cfdeed
ffffff

Requirements
Must have
• Logo
• "Premium Suppliers of Real Time Temperature Tracking"
• Contact Name
• Business Title
• Address
• Telephone
• Mobile
• Email
• Website URL
Nice to have
• Visual representation of tracking or maps.
Should not have
• Image of a satellite as currently shown

```html
<!DOCTYPE html>
<html lang="en">
<head>
<meta charset="utf-8">
<title>Halvor Pinet — Business Card</title>
<link href="https://fonts.googleapis.com/css2?family=Lato:wght@400;700&family=Tinos:wght@400;700&display=swap" rel="stylesheet">
<style>
  :root {
    --backdrop: #d3d3d3;
    --card-white: #ffffff;
    --brand-blue: #2f6cbf;
    --deep-blue: #0a3a8c;
    --ink: #1e1e1e;
    --night: #06204f;
    --glow: #6fb4f5;
  }
  * { margin: 0; padding: 0; box-sizing: border-box; }
  html, body { width: 1200px; height: 900px; overflow: hidden; }
  body { background: var(--backdrop); position: relative; font-family: "Lato", sans-serif; }

  .card {
    position: absolute; top: 306px; width: 439px; height: 272px;
    box-shadow: 3px 3px 6px rgba(0,0,0,0.35);
    overflow: hidden;
  }
  .card-front { left: 150px; background: var(--card-white); }
  .card-back { left: 609px; }

  .corner-mark { position: absolute; left: 0; top: 26px; }
  .holder { position: absolute; left: 36px; top: 27px; }
  .holder-name { font-size: 19px; color: var(--brand-blue); font-weight: 400; line-height: 1.1; }
  .holder-title { font-size: 12px; color: var(--ink); line-height: 1.2; }

  .company-name {
    position: absolute; right: 26px; top: 95px;
    font-size: 31px; font-weight: 700; color: var(--brand-blue); letter-spacing: -0.5px;
  }

  .contact-list { position: absolute; left: 28px; top: 181px; list-style: none; }
  .contact-list li { display: flex; align-items: center; height: 16px; font-size: 12.5px; color: var(--ink); }
  .contact-list svg { width: 10px; height: 10px; margin-right: 6px; fill: var(--deep-blue); }

  .address { position: absolute; right: 26px; top: 211px; text-align: right; font-size: 12.5px; line-height: 16px; color: var(--ink); }

  .base-band { position: absolute; left: 0; bottom: 0; }

  .globe-visual {
    position: absolute; inset: 0;
    background:
      radial-gradient(circle at 50% 35%, rgba(255,255,255,0.9) 0, rgba(160,210,255,0.6) 4%, transparent 18%),
      radial-gradient(circle at 105% 100%, #1d72d6 0, #1258b8 35%, rgba(9,50,120,0) 62%),
      linear-gradient(100deg, var(--night) 0%, #0b3778 45%, #0e4ea6 100%);
  }
  .tagline {
    position: absolute; left: 19px; top: 154px; list-style: none;
    font-family: "Tinos", serif; font-weight: 700; font-size: 11.5px; letter-spacing: 0.6px;
    color: #ffffff; text-transform: uppercase;
  }
  .tagline li { height: 26.5px; }
</style>
</head>
<body>

  <section class="card card-front" aria-label="Card front">
    <svg class="corner-mark" width="30" height="37" viewBox="0 0 30 37" aria-hidden="true">
      <polygon points="0,0 12,0 16,37 0,37" fill="var(--deep-blue)"/>
      <polygon points="13,0 28,0 28,37 17,37" fill="var(--ink)"/>
    </svg>
    <div class="holder">
      <p class="holder-name">Maren Oakes</p>
      <p class="holder-title">Managing Director</p>
    </div>

    <p class="company-name">Halvor Pinet</p>

    <ul class="contact-list">
      <li><svg viewBox="0 0 10 10"><rect x="2.5" y="0" width="5" height="10" rx="1"/><rect x="3.5" y="1.5" width="3" height="6" fill="#fff"/></svg>044-987 650 312</li>
      <li><svg viewBox="0 0 10 10"><path d="M0 3 Q5 -1 10 3 L8 4.5 L6.5 3 L3.5 3 L2 4.5 Z"/><rect x="1.5" y="5" width="7" height="4.5" rx="1"/></svg>044-987 650 312</li>
      <li><svg viewBox="0 0 10 10"><rect x="0" y="2" width="10" height="6.5"/><polyline points="0.5,2.5 5,6 9.5,2.5" fill="none" stroke="#fff" stroke-width="1"/></svg>info@halvorpinet.com</li>
      <li><svg viewBox="0 0 10 10"><circle cx="5" cy="5" r="5"/><path d="M3 2.5 Q5 3.5 4 5 Q6 6 5.5 8.5" fill="none" stroke="#fff" stroke-width="1"/></svg>www.halvorpinet.com</li>
    </ul>

    <p class="address">48 Carrow Street<br>Brisbane, QLD 4000</p>

    <svg class="base-band" width="439" height="21" viewBox="0 0 439 21" aria-hidden="true">
      <polygon points="0,6 217,6 204,21 0,21" fill="var(--deep-blue)"/>
      <polygon points="223,0 439,0 439,21 206,21" fill="var(--ink)"/>
    </svg>
  </section>

  <section class="card card-back" aria-label="Card back">
    <div class="globe-visual" role="img" aria-label="Glowing blue globe with network connection lines over a starry night sky"></div>
    <ul class="tagline">
      <li>Premium Suppliers</li>
      <li>of Real Time</li>
      <li>Temperature</li>
      <li>Tracking</li>
    </ul>
  </section>

</body>
</html>
```